Corvanta512 Business Card Redesign

I want to create a design for brand new business cards, I need something exceptional for clear plastic business card design. Please do not submit without it being on a clear design. Photos of the various logo versions attached.

```html
<!DOCTYPE html>
<html lang="en">
<head>
<meta charset="utf-8">
<title>Corvanta512 Business Card</title>
<link rel="stylesheet" href="https://fonts.googleapis.com/css2?family=Poppins:wght@400;600;700&display=swap">
<style>
  :root {
    --gold: #dfc17c;
    --navy: #324a72;
    --white: #ffffff;
    --ink: #2d2d33;
    --backdrop: #dcdcdc;
  }
  * { margin: 0; padding: 0; box-sizing: border-box; }
  html, body { width: 1200px; height: 1200px; overflow: hidden; }
  body {
    background: var(--backdrop);
    font-family: "Poppins", sans-serif;
    position: relative;
  }
  .card {
    position: absolute;
    left: 150px;
    width: 900px;
    height: 514px;
    overflow: hidden;
  }
  .card--front { top: 65px; }
  .card--back { top: 621px; }
  .card__art { position: absolute; inset: 0; width: 900px; height: 514px; display: block; }

  .holder { position: absolute; left: 69px; top: 88px; }
  .holder__name {
    font-size: 40px; font-weight: 700; color: var(--navy);
    letter-spacing: 0.5px; line-height: 1;
  }
  .holder__role { margin-top: 14px; font-size: 22px; color: var(--ink); line-height: 1; }
  .holder__rule { margin-top: 32px; width: 120px; height: 3px; background: var(--navy); }

  .contact { position: absolute; left: 69px; top: 258px; list-style: none; }
  .contact__item {
    display: flex; align-items: center; gap: 14px;
    font-size: 23px; color: var(--ink); height: 36px;
  }
  .contact__item svg { width: 20px; height: 20px; fill: var(--navy); flex: none; }
  .contact__item--address { align-items: flex-start; height: auto; margin-top: 22px; line-height: 36px; }
  .contact__item--address svg { margin-top: 8px; }

  .brand {
    position: absolute; display: flex; align-items: center; gap: 14px;
    font-family: "Poppins", sans-serif; font-weight: 600; color: var(--navy);
    transform: translate(-50%, -50%); white-space: nowrap;
  }
  .brand__dot { width: 34px; height: 34px; border-radius: 50%; background: var(--gold); flex: none; }
  .brand--front { left: 706px; top: 300px; font-size: 46px; }
  .brand--back { left: 450px; top: 270px; font-size: 58px; }
  .brand--back .brand__dot { width: 44px; height: 44px; }
</style>
</head>
<body>

<section class="card card--front">
  <svg class="card__art" viewBox="0 0 900 514" aria-hidden="true">
    <rect width="900" height="514" fill="var(--gold)"/>
    <ellipse cx="790" cy="250" rx="355" ry="350" fill="var(--white)"/>
    <ellipse cx="820" cy="262" rx="335" ry="290" fill="var(--navy)"/>
    <ellipse cx="860" cy="258" rx="330" ry="255" fill="var(--white)"/>
  </svg>

  <div class="holder">
    <h1 class="holder__name">DANA KELLER</h1>
    <p class="holder__role">Sales &amp; Estimating</p>
    <div class="holder__rule"></div>
  </div>

  <ul class="contact">
    <li class="contact__item">
      <svg viewBox="0 0 24 24"><path d="M6.6 10.8a15 15 0 0 0 6.6 6.6l2.2-2.2c.3-.3.7-.4 1-.2 1.1.4 2.3.6 3.6.6.6 0 1 .4 1 1V20c0 .6-.4 1-1 1A17 17 0 0 1 3 4c0-.6.4-1 1-1h3.5c.6 0 1 .4 1 1 0 1.3.2 2.5.6 3.6.1.3 0 .7-.2 1z"/></svg>
      <span>(555) 010-0000</span>
    </li>
    <li class="contact__item">
      <svg viewBox="0 0 24 24"><path d="M6 2h12v5H6zM4 8h16a2 2 0 0 1 2 2v7h-4v5H6v-5H2v-7a2 2 0 0 1 2-2zm4 7v5h8v-5z"/></svg>
      <span>(555) 010-0000</span>
    </li>
    <li class="contact__item">
      <svg viewBox="0 0 24 24"><path d="M3 5h18v14H3zm2 2v.5l7 5 7-5V7z"/></svg>
      <span>www.corvanta512.com</span>
    </li>
    <li class="contact__item contact__item--address">
      <svg viewBox="0 0 24 24"><path d="M12 2a7 7 0 0 1 7 7c0 5-7 13-7 13S5 14 5 9a7 7 0 0 1 7-7zm0 4.5A2.5 2.5 0 1 0 12 11.5 2.5 2.5 0 0 0 12 6.5z"/></svg>
      <span>0/4 Harlow Blvd Suite 0418,<br>Millbrook, PA 11302</span>
    </li>
  </ul>

  <div class="brand brand--front"><span class="brand__dot"></span>Corvanta512</div>
</section>

<section class="card card--back">
  <svg class="card__art" viewBox="0 0 900 514" aria-hidden="true">
    <rect width="900" height="514" fill="var(--white)"/>
    <path d="M0 0 H470 Q170 120 40 514 H0 Z" fill="var(--gold)"/>
    <ellipse cx="506" cy="262" rx="372" ry="262" transform="rotate(-12 506 262)" fill="var(--navy)"/>
    <ellipse cx="536" cy="252" rx="345" ry="240" transform="rotate(-12 536 252)" fill="var(--white)"/>
  </svg>

  <div class="brand brand--back"><span class="brand__dot"></span>Corvanta512</div>
</section>

</body>
</html>
```